Bright Harbor need a basic Calendar design

Our customers like when we give them a calendar every year but we have undergone some changes in our branding and we seek a similar product to what we delivered, but with new logos and a fresh look. If you can incorporate some stock imagery or something that is fine (like the attached apples but not necessarily that image, thats fine). This is a basic corporate calendar,

See attached photos for what we are looking for. Essentially the same exact type of wall calendar with new logo and images. That is all.

Industry/Entity Type

Product

Font styles to use
Serif
Sans Serif

Colors
3277b5
0355a3
85abd2
ffffff

```html
<!DOCTYPE html>
<html lang="en">
<head>
<meta charset="utf-8">
<title>Bright Harbor 2015 Wall Calendar</title>
<link rel="stylesheet" href="https://fonts.googleapis.com/css2?family=Open+Sans:wght@400;600;700;800&family=Poppins:wght@800;900&display=swap">
<style>
  :root {
    --page: #ffffff;
    --apple-light: #c9dc6a;
    --apple-mid: #8db83a;
    --apple-dark: #4f7a1c;
    --month: #5e2a84;
    --date: #5a5a5a;
    --weekday: #7a7a7a;
    --holiday: #d9d2e6;
    --brand: #0355a3;
    --brand-light: #3277b5;
    --tagline: #85abd2;
  }
  * { box-sizing: border-box; margin: 0; padding: 0; }
  html, body { width: 900px; height: 1200px; overflow: hidden; background: var(--page); }
  .calendar { position: relative; width: 900px; height: 1200px; font-family: "Open Sans", Arial, sans-serif; }

  .hero {
    position: absolute; left: 0; top: 0; width: 900px; height: 330px;
    background: radial-gradient(circle at 20% 30%, var(--apple-light), transparent 40%),
                radial-gradient(circle at 75% 70%, var(--apple-light), transparent 45%),
                linear-gradient(160deg, var(--apple-mid), var(--apple-dark));
  }
  .year {
    position: absolute; left: 0; top: 70px; width: 900px; text-align: center;
    font-family: "Poppins", Arial, sans-serif; font-weight: 900; font-size: 190px; line-height: 1;
    letter-spacing: 4px;
    background: linear-gradient(180deg, #eaf4b8 0%, #9cc447 45%, #3f6b12 100%);
    -webkit-background-clip: text; background-clip: text; color: transparent;
    -webkit-text-stroke: 3px #f4f8e4;
    filter: drop-shadow(4px 6px 4px rgba(30,50,10,.6));
  }

  .months {
    position: absolute; left: 30px; top: 352px; width: 850px;
    display: grid; grid-template-columns: repeat(4, 212px); grid-template-rows: repeat(3, 282px);
  }
  .month-name { font-weight: 700; font-size: 30px; color: var(--month); line-height: 38px; text-transform: lowercase; }
  .weekdays, .days { display: grid; grid-template-columns: repeat(7, 27px); list-style: none; }
  .weekdays { font-size: 11px; color: var(--weekday); margin: 4px 0 4px; }
  .weekdays li { text-align: center; }
  .days li {
    width: 24px; height: 24px; line-height: 24px; margin: 2px 0; text-align: center;
    font-size: 14px; color: var(--date);
  }
  .days li.holiday { background: var(--holiday); border-radius: 50%; }
  .s1 > :first-child { grid-column-start: 2; }
  .s2 > :first-child { grid-column-start: 3; }
  .s3 > :first-child { grid-column-start: 4; }
  .s4 > :first-child { grid-column-start: 5; }
  .s5 > :first-child { grid-column-start: 6; }
  .s6 > :first-child { grid-column-start: 7; }

  .brand {
    position: absolute; left: 0; top: 1118px; width: 900px; text-align: center;
  }
  .brand-line { display: inline-flex; align-items: center; gap: 10px; }
  .brand-dot { width: 26px; height: 26px; border-radius: 50%; background: var(--brand-light); }
  .brand-name { font-weight: 700; font-size: 30px; color: var(--brand); }
  .brand-tagline { font-size: 12px; font-style: italic; color: var(--brand-light); margin-top: 2px; }
</style>
</head>
<body>
<div class="calendar">
  <div class="hero" role="img" aria-label="Photograph of rows of green apples with a single red apple"></div>
  <div class="year">2015</div>

  <div class="months">
    <section class="month"><h2 class="month-name">january</h2>
      <ul class="weekdays"><li>s</li><li>m</li><li>t</li><li>w</li><li>t</li><li>f</li><li>s</li></ul>
      <ol class="days s4"><li class="holiday">1</li><li>2</li><li>3</li><li>4</li><li>5</li><li>6</li><li>7</li><li>8</li><li>9</li><li>10</li><li>11</li><li>12</li><li>13</li><li>14</li><li>15</li><li>16</li><li>17</li><li>18</li><li class="holiday">19</li><li>20</li><li>21</li><li>22</li><li>23</li><li>24</li><li>25</li><li>26</li><li>27</li><li>28</li><li>29</li><li>30</li><li>31</li></ol>
    </section>
    <section class="month"><h2 class="month-name">february</h2>
      <ul class="weekdays"><li>s</li><li>m</li><li>t</li><li>w</li><li>t</li><li>f</li><li>s</li></ul>
      <ol class="days"><li>1</li><li>2</li><li>3</li><li>4</li><li>5</li><li>6</li><li>7</li><li>8</li><li>9</li><li>10</li><li>11</li><li>12</li><li>13</li><li>14</li><li>15</li><li class="holiday">16</li><li>17</li><li>18</li><li>19</li><li>20</li><li>21</li><li>22</li><li>23</li><li>24</li><li>25</li><li>26</li><li>27</li><li>28</li></ol>
    </section>
    <section class="month"><h2 class="month-name">march</h2>
      <ul class="weekdays"><li>s</li><li>m</li><li>t</li><li>w</li><li>t</li><li>f</li><li>s</li></ul>
      <ol class="days"><li>1</li><li>2</li><li>3</li><li>4</li><li>5</li><li>6</li><li>7</li><li>8</li><li>9</li><li>10</li><li>11</li><li>12</li><li>13</li><li>14</li><li>15</li><li>16</li><li>17</li><li>18</li><li>19</li><li>20</li><li>21</li><li>22</li><li>23</li><li>24</li><li>25</li><li>26</li><li>27</li><li>28</li><li>29</li><li>30</li><li>31</li></ol>
    </section>
    <section class="month"><h2 class="month-name">april</h2>
      <ul class="weekdays"><li>s</li><li>m</li><li>t</li><li>w</li><li>t</li><li>f</li><li>s</li></ul>
      <ol class="days s3"><li>1</li><li>2</li><li>3</li><li>4</li><li class="holiday">5</li><li>6</li><li>7</li><li>8</li><li>9</li><li>10</li><li>11</li><li>12</li><li>13</li><li>14</li><li>15</li><li>16</li><li>17</li><li>18</li><li>19</li><li>20</li><li>21</li><li>22</li><li>23</li><li>24</li><li>25</li><li>26</li><li>27</li><li>28</li><li>29</li><li>30</li></ol>
    </section>

    <section class="month"><h2 class="month-name">may</h2>
      <ul class="weekdays"><li>s</li><li>m</li><li>t</li><li>w</li><li>t</li><li>f</li><li>s</li></ul>
      <ol class="days s5"><li>1</li><li>2</li><li>3</li><li>4</li><li>5</li><li>6</li><li>7</li><li>8</li><li>9</li><li>10</li><li>11</li><li>12</li><li>13</li><li>14</li><li>15</li><li>16</li><li>17</li><li>18</li><li>19</li><li>20</li><li>21</li><li>22</li><li>23</li><li>24</li><li class="holiday">25</li><li>26</li><li>27</li><li>28</li><li>29</li><li>30</li><li>31</li></ol>
    </section>
    <section class="month"><h2 class="month-name">june</h2>
      <ul class="weekdays"><li>s</li><li>m</li><li>t</li><li>w</li><li>t</li><li>f</li><li>s</li></ul>
      <ol class="days s1"><li>1</li><li>2</li><li>3</li><li>4</li><li>5</li><li>6</li><li>7</li><li>8</li><li>9</li><li>10</li><li>11</li><li>12</li><li>13</li><li>14</li><li>15</li><li>16</li><li>17</li><li>18</li><li>19</li><li>20</li><li>21</li><li>22</li><li>23</li><li>24</li><li>25</li><li>26</li><li>27</li><li>28</li><li>29</li><li>30</li></ol>
    </section>
    <section class="month"><h2 class="month-name">july</h2>
      <ul class="weekdays"><li>s</li><li>m</li><li>t</li><li>w</li><li>t</li><li>f</li><li>s</li></ul>
      <ol class="days s3"><li>1</li><li>2</li><li class="holiday">3</li><li>4</li><li>5</li><li>6</li><li>7</li><li>8</li><li>9</li><li>10</li><li>11</li><li>12</li><li>13</li><li>14</li><li>15</li><li>16</li><li>17</li><li>18</li><li>19</li><li>20</li><li>21</li><li>22</li><li>23</li><li>24</li><li>25</li><li>26</li><li>27</li><li>28</li><li>29</li><li>30</li><li>31</li></ol>
    </section>
    <section class="month"><h2 class="month-name">august</h2>
      <ul class="weekdays"><li>s</li><li>m</li><li>t</li><li>w</li><li>t</li><li>f</li><li>s</li></ul>
      <ol class="days s6"><li>1</li><li>2</li><li>3</li><li>4</li><li>5</li><li>6</li><li>7</li><li>8</li><li>9</li><li>10</li><li>11</li><li>12</li><li>13</li><li>14</li><li>15</li><li>16</li><li>17</li><li>18</li><li>19</li><li>20</li><li>21</li><li>22</li><li>23</li><li>24</li><li>25</li><li>26</li><li>27</li><li>28</li><li>29</li><li>30</li><li>31</li></ol>
    </section>

    <section class="month"><h2 class="month-name">september</h2>
      <ul class="weekdays"><li>s</li><li>m</li><li>t</li><li>w</li><li>t</li><li>f</li><li>s</li></ul>
      <ol class="days s2"><li>1</li><li>2</li><li>3</li><li>4</li><li>5</li><li>6</li><li class="holiday">7</li><li>8</li><li>9</li><li>10</li><li>11</li><li>12</li><li>13</li><li>14</li><li>15</li><li>16</li><li>17</li><li>18</li><li>19</li><li>20</li><li>21</li><li>22</li><li>23</li><li>24</li><li>25</li><li>26</li><li>27</li><li>28</li><li>29</li><li>30</li></ol>
    </section>
    <section class="month"><h2 class="month-name">october</h2>
      <ul class="weekdays"><li>s</li><li>m</li><li>t</li><li>w</li><li>t</li><li>f</li><li>s</li></ul>
      <ol class="days s4"><li>1</li><li>2</li><li>3</li><li>4</li><li>5</li><li>6</li><li>7</li><li>8</li><li>9</li><li>10</li><li>11</li><li class="holiday">12</li><li>13</li><li>14</li><li>15</li><li>16</li><li>17</li><li>18</li><li>19</li><li>20</li><li>21</li><li>22</li><li>23</li><li>24</li><li>25</li><li>26</li><li>27</li><li>28</li><li>29</li><li>30</li><li>31</li></ol>
    </section>
    <section class="month"><h2 class="month-name">november</h2>
      <ul class="weekdays"><li>s</li><li>m</li><li>t</li><li>w</li><li>t</li><li>f</li><li>s</li></ul>
      <ol class="days"><li>1</li><li>2</li><li>3</li><li>4</li><li>5</li><li>6</li><li>7</li><li>8</li><li>9</li><li>10</li><li class="holiday">11</li><li>12</li><li>13</li><li>14</li><li>15</li><li>16</li><li>17</li><li>18</li><li>19</li><li>20</li><li>21</li><li>22</li><li>23</li><li>24</li><li>25</li><li class="holiday">26</li><li>27</li><li>28</li><li>29</li><li>30</li></ol>
    </section>
    <section class="month"><h2 class="month-name">december</h2>
      <ul class="weekdays"><li>s</li><li>m</li><li>t</li><li>w</li><li>t</li><li>f</li><li>s</li></ul>
      <ol class="days s2"><li>1</li><li>2</li><li>3</li><li>4</li><li>5</li><li>6</li><li>7</li><li>8</li><li>9</li><li>10</li><li>11</li><li>12</li><li>13</li><li>14</li><li>15</li><li>16</li><li>17</li><li>18</li><li>19</li><li>20</li><li>21</li><li>22</li><li>23</li><li>24</li><li class="holiday">25</li><li>26</li><li>27</li><li>28</li><li>29</li><li>30</li><li>31</li></ol>
    </section>
  </div>

  <footer class="brand">
    <div class="brand-line"><span class="brand-dot"></span><span class="brand-name">Bright Harbor</span></div>
    <p class="brand-tagline">Coastal Services Group, LLC</p>
  </footer>
</div>
</body>
</html>
```